Halvorsen Partners Business Card

Halvorsen Partners Civil Construction
Dorian Halvorsen
CEO
555-318-4076
Dorian@HalvorsenCivil.example
www.HalvorsenCivil.example
Site Development
Utility Construction
Excavation
48730 County Route 19
Land O' Lakes, FL 34999

Target Market(s)

Construction and government

Industry/Entity Type

Business

Contact Information for Business Card

I want an unique design that make a statement

Number of Pages Required

1 page

Font styles to use
Other font styles liked:

Colors

Designer to choose colors to be used in the design.

Requirements
Must have
• unique design, feel free to modify or change the color of my logo.
Nice to have
• extra design features like spot UV, foil accents, color edges, unique paper, or any thing that would make my card pop.
• I like the feel of the image that I attached

```html
<!DOCTYPE html>
<html lang="en">
<head>
<meta charset="utf-8">
<title>Halvorsen Partners Business Card</title>
<link rel="stylesheet" href="https://fonts.googleapis.com/css2?family=Lato:wght@400;700&display=swap">
<style>
  :root {
    --stage: #2b2b2d;
    --brand-blue: #1f3f8f;
    --brand-blue-light: #2f62d6;
    --brand-blue-dark: #1a3170;
    --band-grey: #5e5f61;
    --paper: #f4f4f4;
    --ink-grey: #6b6d70;
    --white: #ffffff;
  }
  * { box-sizing: border-box; margin: 0; padding: 0; }
  html, body {
    width: 1200px; height: 900px; overflow: hidden;
    background: var(--stage);
    font-family: "Lato", sans-serif;
  }
  .stage {
    width: 1200px; height: 900px;
    display: flex; flex-direction: column;
    align-items: center; justify-content: center; gap: 40px;
  }
  .card {
    width: 700px; height: 400px;
    position: relative; overflow: hidden;
    box-shadow: 0 10px 30px rgba(0,0,0,.45);
  }

  /* Brand lockup */
  .brand {
    display: flex; align-items: center; gap: 16px;
  }
  .brand-square {
    width: 46px; height: 46px; flex: none;
  }
  .brand-name {
    font-weight: 400; letter-spacing: 2px; text-transform: uppercase;
    line-height: 1.15;
  }
  .brand-name .line-main { display: block; font-size: 30px; }
  .brand-name .line-sub { display: block; font-size: 17px; letter-spacing: 5px; }

  /* Back of card */
  .card-back {
    background: linear-gradient(120deg, var(--brand-blue-light) 0%, var(--brand-blue) 45%, var(--brand-blue-dark) 100%);
    display: flex; align-items: center; justify-content: center;
  }
  .card-back .brand-square { background: var(--white); }
  .card-back .brand-name { color: var(--white); }

  /* Front of card */
  .card-front { background: var(--paper); display: flex; flex-direction: column; }
  .front-identity {
    height: 220px; display: flex; align-items: center; justify-content: center;
  }
  .card-front .brand-square { background: var(--brand-blue); }
  .card-front .brand-name { color: var(--brand-blue); }
  .name-band {
    height: 50px; background: var(--band-grey);
    display: flex; align-items: center; justify-content: center;
    color: var(--white); font-size: 20px; letter-spacing: .5px;
  }
  .name-band .person { font-weight: 700; text-transform: uppercase; }
  .name-band .role { font-weight: 400; font-size: 16px; margin-left: 6px; }
  .contact-panel {
    flex: 1; background: linear-gradient(120deg, var(--brand-blue-dark), var(--brand-blue) 60%, var(--brand-blue-light));
    color: var(--white); text-align: center;
    display: flex; flex-direction: column; justify-content: center; gap: 6px;
    font-size: 17px;
  }
  .services .dot {
    display: inline-block; width: 7px; height: 7px; background: var(--white);
    margin: 0 8px; vertical-align: middle;
  }
</style>
</head>
<body>
<main class="stage">
  <section class="card card-back">
    <div class="brand">
      <span class="brand-square"></span>
      <span class="brand-name">
        <span class="line-main">Halvorsen Partners</span>
        <span class="line-sub">Civil Construction</span>
      </span>
    </div>
  </section>

  <section class="card card-front">
    <div class="front-identity">
      <div class="brand">
        <span class="brand-square"></span>
        <span class="brand-name">
          <span class="line-main">Halvorsen Partners</span>
          <span class="line-sub">Civil Construction</span>
        </span>
      </div>
    </div>
    <div class="name-band">
      <span class="person">Dorian Halvorsen</span><span class="role">- CEO</span>
    </div>
    <div class="contact-panel">
      <p class="services">Site Development<span class="dot"></span>Utility Construction<span class="dot"></span>Excavation</p>
      <p class="contacts">P: 555-318-4076 &nbsp;E: Dorian@HalvorsenCivil.example</p>
      <p class="web">W: www.HalvorsenCivil.example</p>
    </div>
  </section>
</main>
</body>
</html>
```